Web Design for an Online Dating Web Site

We need an uncoded web design for a new online dating web site called zMatchy.net. Simplicity and boldness are the key factors in the successful design.
Please look at the requirements document attached for details.
Updates
Dear all,
Please AVOID USING A PICTURE OF A HAPPY COUPLE ON THE HOME PAGE of the site. We highly want to move away from this space as it makes our web site just like another dating web site.
We like something simple with web 2.0 look and feel. The examples in the Requirements Document are exactly the design we are after.
Regards
Tarn
Industry/Entity Type
Dating
Look and feel
Each slider illustrates characteristics of the customer's brand and the style your logo design should communicate.

```html
<!DOCTYPE html>
<html lang="en">
<head>
<meta charset="utf-8">
<title>zMatchy.net — Home</title>
<link rel="stylesheet" href="https://fonts.googleapis.com/css2?family=Oswald:wght@300;400&family=Noto+Sans&family=Ubuntu:wght@400;500&display=swap">
<style>
  :root {
    --cyan: #7fdde8;
    --cyan-pale: #bff2f6;
    --pink: #e0097a;
    --pink-mid: #c0006a;
    --pink-deep: #7e003e;
    --pink-logo: #e8137f;
    --teal-text: #39b6cc;
    --yellow: #f5f07a;
    --grey-text: #7b7b7b;
    --footer-a: #4a4a4a;
    --footer-b: #8a8c8e;
    --white: #ffffff;
  }
  * { box-sizing: border-box; margin: 0; padding: 0; }
  html, body { width: 960px; height: 1200px; overflow: hidden; }
  body { position: relative; background: var(--cyan); font-family: 'Noto Sans', sans-serif; }

  .header-band { position: absolute; left: 0; top: 0; width: 960px; height: 200px; background: linear-gradient(#a4ebf1, #7ad9e5); }
  .nav-strip { position: absolute; left: 0; top: 104px; width: 560px; height: 50px; background: rgba(255,255,255,.18); }
  .hero-band { position: absolute; left: 0; top: 196px; width: 960px; height: 356px; background: radial-gradient(ellipse at 50% 50%, var(--pink) 0%, var(--pink-mid) 60%, var(--pink-deep) 100%); border-top: 3px solid var(--cyan-pale); border-bottom: 3px solid var(--cyan-pale); }
  .video-band { position: absolute; left: 0; top: 555px; width: 960px; height: 485px; background: linear-gradient(#a4ecf2, #86dde8 60%, #a8edf3); }
  .video-glow { position: absolute; left: 150px; top: 585px; width: 660px; height: 320px; border-radius: 50%; background: radial-gradient(ellipse at center, #fff 0%, #fff 50%, rgba(255,255,255,0) 100%); }

  .brand { position: absolute; left: 96px; top: 28px; font-family: 'Ubuntu', sans-serif; font-weight: 500; font-size: 40px; color: var(--pink-logo); display: flex; align-items: center; gap: 8px; }
  .brand-dot { width: 14px; height: 14px; border-radius: 50%; background: var(--pink-logo); }

  .main-nav { position: absolute; left: 94px; top: 119px; display: flex; gap: 23px; font-family: 'Oswald', sans-serif; font-weight: 300; font-size: 15px; letter-spacing: .3px; }
  .main-nav a { color: var(--white); text-decoration: none; text-shadow: 0 1px 1px rgba(0,90,110,.35); }
  .main-nav a.is-active { color: var(--yellow); }

  .login-box { position: absolute; left: 559px; top: 24px; width: 304px; height: 126px; background: var(--white); border-radius: 4px; box-shadow: 0 2px 4px rgba(0,80,100,.25); }
  .login-title { position: absolute; left: 13px; top: 15px; font-family: 'Oswald', sans-serif; font-weight: 400; font-size: 17px; color: var(--teal-text); display: flex; align-items: center; gap: 7px; }
  .login-title span { color: var(--pink); margin-left: -3px; }
  .lock { width: 12px; height: 12px; }
  .field { position: absolute; top: 46px; width: 134px; height: 24px; background: linear-gradient(#eeeeee, #f8f8f8); border: 1px solid #e4e4e4; font-size: 9.5px; font-style: italic; color: #8a8a8a; padding: 5px 11px; }
  .field-user { left: 12px; }
  .field-pass { left: 158px; }
  .login-btn { position: absolute; left: 13px; top: 82px; width: 81px; height: 24px; border-radius: 4px; background: linear-gradient(#e6e6e6, #b8b8b8); border: 1px solid #9f9f9f; font-family: 'Oswald', sans-serif; font-weight: 300; font-size: 12px; color: #555; text-align: center; line-height: 22px; }
  .login-or { position: absolute; left: 107px; top: 84px; font-size: 14px; font-weight: bold; font-style: italic; color: #666; }
  .provider-list { position: absolute; left: 134px; top: 88px; display: flex; gap: 6px; font-size: 8.5px; color: #555; align-items: center; list-style: none; }
  .provider-list li { display: flex; align-items: center; gap: 3px; }
  .provider-list i { display: block; width: 6px; height: 6px; background: var(--pink); }
  .login-more { position: absolute; left: 252px; top: 85px; font-size: 11.5px; color: var(--pink); border-left: 1px solid #ddd; padding-left: 7px; }

  .slide-photo { position: absolute; left: 96px; top: 245px; width: 413px; height: 240px; background: radial-gradient(ellipse at 45% 45%, #ffd3ea 0%, #fff4fa 45%, #ffffff 75%); box-shadow: 0 16px 14px -10px rgba(40,0,20,.55); }
  .slide-title { position: absolute; left: 534px; top: 258px; font-family: 'Oswald', sans-serif; font-weight: 400; font-size: 34px; line-height: 44px; color: var(--white); }
  .slide-text { position: absolute; left: 535px; top: 309px; width: 340px; font-size: 15.5px; line-height: 19.5px; color: #fbe2ef; }
  .pill-btn { position: absolute; left: 545px; top: 415px; width: 208px; height: 52px; border-radius: 26px; background: linear-gradient(#efefef, #bdbdbd); box-shadow: 0 0 10px rgba(255,120,190,.7); font-family: 'Oswald', sans-serif; font-weight: 400; font-size: 26px; color: var(--grey-text); text-align: center; line-height: 52px; }
  .slide-arrow { position: absolute; top: 339px; width: 48px; height: 48px; }
  .slide-arrow.prev { left: 12px; }
  .slide-arrow.next { left: 900px; }

  .play-btn { position: absolute; left: 434px; top: 698px; width: 92px; height: 92px; }
  .signup-btn { position: absolute; left: 357px; top: 925px; width: 264px; height: 73px; background: linear-gradient(#ececec, #b7b7b7); border-radius: 3px; box-shadow: 0 3px 5px rgba(0,60,80,.35); font-family: 'Oswald', sans-serif; font-weight: 400; font-size: 44px; color: #6f6f6f; text-align: center; line-height: 73px; }
  .hint-area { position: absolute; left: 636px; top: 876px; width: 116px; height: 122px; border-radius: 50%; background: radial-gradient(ellipse at center, rgba(255,255,255,.75) 0%, rgba(255,255,255,0) 70%); }

  .site-footer { position: absolute; left: 0; top: 1040px; width: 960px; height: 160px; background: linear-gradient(90deg, var(--footer-a), var(--footer-b) 55%, var(--footer-a)); border-top: 2px solid #9a9a9a; }
  .footer-brand { position: absolute; left: 96px; top: 66px; font-family: 'Ubuntu', sans-serif; font-weight: 500; font-size: 28px; color: #a5a5a5; display: flex; align-items: center; gap: 6px; }
  .footer-brand i { width: 10px; height: 10px; border-radius: 50%; background: #a5a5a5; }
  .footer-col { position: absolute; top: 22px; }
  .footer-col.links { left: 364px; width: 186px; }
  .footer-col.talk { left: 593px; width: 186px; }
  .footer-heading { font-family: 'Oswald', sans-serif; font-weight: 400; font-size: 13px; color: var(--white); padding-bottom: 5px; border-bottom: 1px solid #8e8e8e; }
  .footer-heading span { color: #b4b4b4; font-weight: 300; }
  .footer-links { list-style: none; margin-top: 10px; font-family: 'Ubuntu', sans-serif; font-size: 10.5px; line-height: 14.5px; color: var(--white); }
  .social-row { display: flex; gap: 6px; margin-top: 14px; list-style: none; }
  .social-row li { width: 26px; height: 26px; border-radius: 3px; background: #e8e8e8; font-family: 'Ubuntu', sans-serif; font-size: 6.5px; color: #444; display: flex; align-items: center; justify-content: center; }
  .share-row { display: flex; gap: 6px; margin-top: 10px; justify-content: center; font-family: 'Ubuntu', sans-serif; font-size: 8px; }
  .share-row span { background: #eef3fa; border: 1px solid #aab8cf; color: #3b5a8a; padding: 2px 5px; border-radius: 2px; }
  .share-row b { font-weight: 400; background: #fff; border: 1px solid #aab8cf; color: #3b5a8a; padding: 2px 3px; border-radius: 2px; }
  .share-row.second { margin-top: 6px; }
</style>
</head>
<body>
<div class="header-band"></div>
<div class="nav-strip"></div>
<div class="hero-band"></div>
<div class="video-band"></div>
<div class="video-glow"></div>

<header>
  <div class="brand">zMatchy.net<i class="brand-dot"></i></div>
  <nav class="main-nav">
    <a class="is-active" href="#">WHY</a>
    <a href="#">HOW IT WORKS</a>
    <a href="#">SIGN UP</a>
    <a href="#">OUR BLOG</a>
  </nav>

  <form class="login-box">
    <div class="login-title">
      <svg class="lock" viewBox="0 0 12 12"><rect x="1" y="5" width="10" height="7" fill="#bbb"/><path d="M3 5V3.5a3 3 0 0 1 6 0V5" fill="none" stroke="#bbb" stroke-width="1.6"/></svg>
      USER <span>LOGIN</span>
    </div>
    <div class="field field-user">username</div>
    <div class="field field-pass">password</div>
    <div class="login-btn">LOGIN</div>
    <div class="login-or">or</div>
    <ul class="provider-list">
      <li><i></i>Postly</li>
      <li>Yodlr</li>
      <li>KeyPass</li>
    </ul>
    <div class="login-more">More</div>
  </form>
</header>

<section class="slider">
  <div class="slide-photo" role="img" aria-label="Illustration of pink heart balloons tied to a computer mouse on white"></div>
  <h2 class="slide-title">KEY DIFFERENCE</h2>
  <p class="slide-text">It is a long established fact that a reader will be distracted by the readable content of a page when looking at its layout.</p>
  <div class="pill-btn">READ MORE</div>
  <svg class="slide-arrow prev" viewBox="0 0 48 48" aria-label="Previous slide">
    <circle cx="24" cy="24" r="22" fill="#e9e9e9"/>
    <path d="M28 14 L18 24 L28 34" fill="none" stroke="var(--pink)" stroke-width="5" stroke-linejoin="round"/>
  </svg>
  <svg class="slide-arrow next" viewBox="0 0 48 48" aria-label="Next slide">
    <circle cx="24" cy="24" r="22" fill="#e9e9e9"/>
    <path d="M20 14 L30 24 L20 34" fill="none" stroke="var(--pink)" stroke-width="5" stroke-linejoin="round"/>
  </svg>
</section>

<section class="video">
  <svg class="play-btn" viewBox="0 0 92 92" aria-label="Play video">
    <circle cx="46" cy="46" r="45" fill="#d2d2d2" stroke="#c0c0c0"/>
    <circle cx="46" cy="46" r="41" fill="#e6e6e6"/>
    <path d="M33 26 L66 46 L33 66 Z" fill="var(--pink)"/>
  </svg>
  <div class="signup-btn">SIGN UP</div>
  <div class="hint-area" role="img" aria-label="Decorative curved arrow pointing to the sign up button"></div>
</section>

<footer class="site-footer">
  <div class="footer-brand">zMatchy.net<i></i></div>
  <div class="footer-col links">
    <h3 class="footer-heading">READ <span>MORE</span></h3>
    <ul class="footer-links">
      <li>Why zMatchy</li>
      <li>How it works</li>
      <li>Sign Up</li>
      <li>Login</li>
      <li>About Us</li>
    </ul>
  </div>
  <div class="footer-col talk">
    <h3 class="footer-heading">LET'S <span>TALK</span></h3>
    <ul class="social-row">
      <li>Chirp</li><li>Face</li><li>Tumb</li><li>Yodlr</li><li>Vidly</li><li>Snapr</li>
    </ul>
    <div class="share-row"><span>Love</span><b>10,000</b><span>Post</span><b>10,000</b></div>
    <div class="share-row second"><span>Plus</span><b>10,000</b></div>
  </div>
</footer>
</body>
</html>
```